Single Page Production Company Site

Clean. Simple. Minimalist site with one page.

No portfolio, just some text to communicate a general overview of what the company does.

We work for a very select group of clients, creating strong brand personalities online. The site is specifically minimal and not communicating too much about what we do.. we have a variety of capabilities to work with clients and prefer to be broad with just a simple landing page as the point of contact for our brand.
Updates

Christmas holidays are coming up, maybe people need some time away from work with family and friends... We can keep working on this and I will provide feedback as quickly as possible, but I understand if designers have other commitments during the coming days. Thanks for your hard work!

Industry/Entity Type

Design Agency

Coding

Coded - Design and coding required

Number of Pages Required

1 page

Font styles to use
Sans Serif

Requirements
Must have
• Clean, bold text headlines.
Nice to have
• Unsure about any images used in the design, would like to see options with or without.

```html
<!DOCTYPE html>
<html lang="en">
<head>
<meta charset="utf-8">
<title>Cedarline Studio</title>
<link href="https://fonts.googleapis.com/css2?family=Josefin+Sans:wght@700&family=Lato:wght@300;400;700&family=Montserrat:wght@700&display=swap" rel="stylesheet">
<style>
:root{
  --coral:#f07070;
  --coral-deep:#d85a5a;
  --slate:#777777;
  --paper:#f2f2f2;
  --ink-soft:#9a9a9a;
  --white:#ffffff;
}
*{box-sizing:border-box;margin:0;padding:0}
html,body{width:1200px;height:2970px;overflow:hidden}
body{position:relative;background:var(--paper);font-family:"Lato",sans-serif;color:var(--ink-soft)}
.abs{position:absolute}

/* hero */
.hero{left:0;top:0;width:1200px;height:505px;background:linear-gradient(100deg,#5a5a5e 0%,#6f6f72 35%,#55575c 65%,#7a7672 100%)}
.hero-title{left:0;top:172px;width:1200px;text-align:center;font-family:"Montserrat",sans-serif;font-weight:700;font-size:26px;line-height:33px;color:var(--white)}
.hero-title em{font-style:normal;color:var(--coral)}
.btn-learn{left:537px;top:296px;width:128px;height:26px;background:#8a8a8a;color:var(--white);font-size:12px;font-weight:700;letter-spacing:1px;text-align:center;line-height:26px;font-family:"Montserrat",sans-serif}
.watch{left:536px;top:352px;color:#d8d8d8;font-size:12px;font-weight:700;letter-spacing:1px;font-family:"Montserrat",sans-serif;display:flex;align-items:center;gap:8px}

/* services */
.services{left:0;top:505px;width:1200px;height:510px;background:var(--slate);color:var(--white)}
.services h2{position:absolute;left:0;top:100px;width:1200px;text-align:center;font-family:"Montserrat",sans-serif;font-size:19px;letter-spacing:1px}
.services .lead{position:absolute;left:0;top:140px;width:1200px;text-align:center;font-size:15px;line-height:21px;letter-spacing:.5px}
.service{position:absolute;width:320px;text-align:center}
.service svg{display:block;margin:0 auto 22px}
.service h3{font-family:"Montserrat",sans-serif;font-size:15px;letter-spacing:.5px;margin-bottom:14px}
.service p{font-size:13px;line-height:16px;letter-spacing:.4px}

/* story */
.photo{background:linear-gradient(120deg,#e8d7c8,#c9a58a 50%,#efe6dd)}
.headline{font-family:"Josefin Sans",sans-serif;font-weight:700;color:var(--coral);text-transform:uppercase;line-height:.86;text-shadow:3px 3px 0 var(--coral-deep)}
.copy{font-weight:300;font-size:15px;line-height:20px;color:var(--ink-soft)}
.btn-outline{width:170px;height:45px;border:3px solid var(--coral);color:var(--coral);font-size:13px;letter-spacing:1px;text-align:center;line-height:39px;font-weight:300}

/* contact */
.contact{left:0;top:2375px;width:1200px;height:485px;background:var(--slate)}
.field{left:398px;width:405px;height:40px;background:var(--white);font-size:12px;color:#aaa;padding:10px 12px;font-weight:300}
.btn-login{left:535px;top:2753px;width:131px;height:42px;background:var(--white);color:#555;font-family:"Montserrat",sans-serif;font-size:14px;text-align:center;line-height:42px;letter-spacing:1px}

/* footer */
.footer-dot{top:2898px;width:26px;height:26px;border-radius:50%;background:var(--coral)}
.legal{right:110px;top:2890px;font-size:13px;font-weight:300;color:var(--ink-soft)}
</style>
</head>
<body>

<section class="abs hero" role="img" aria-label="Photo of a team meeting around a table with a presenter"></section>
<h1 class="abs hero-title">We <em>create</em><br>strong brand personalities<br>online.</h1>
<div class="abs btn-learn">LEARN MORE</div>
<div class="abs watch"><svg width="10" height="12" viewBox="0 0 10 12"><path d="M0 0L10 6L0 12Z" fill="#d8d8d8"/></svg>WATCH VIDEO</div>

<section class="abs services">
  <h2>CONCEPT. CREATE. COMPLETE.</h2>
  <p class="lead">We work for a very select group of clients, creating<br>strong brand personalities online.</p>

  <div class="service" style="left:68px;top:215px">
    <svg width="54" height="54" viewBox="0 0 54 54" fill="none" stroke="#f07070" stroke-width="2">
      <circle cx="27" cy="27" r="12"/><circle cx="27" cy="27" r="4"/>
      <path d="M27 8v7M27 39v7M8 27h7M39 27h7M14 14l5 5M35 35l5 5M40 14l-5 5M14 40l5-5"/>
    </svg>
    <h3>DESIGN HAPPENS HERE</h3>
    <p>We are leading the way in design<br>innovation for modern websites.<br>Clean, functional, intuitive websites<br>for progressive businesses.</p>
  </div>

  <div class="service" style="left:440px;top:215px">
    <svg width="54" height="54" viewBox="0 0 54 54" fill="none" stroke="#f07070" stroke-width="2.5">
      <path d="M32 10H8v36h36V22"/><path d="M22 32l2-8L44 4l6 6L30 30z"/>
    </svg>
    <h3 style="margin-top:6px">ART HAPPENS HERE</h3>
    <p>Building brands through design, we believe<br>that contrast is everything. For industry<br>leaders who set the pace and exceed<br>expectations, we help give the company<br>voice and soul.</p>
  </div>

  <div class="service" style="left:797px;top:215px">
    <svg width="50" height="54" viewBox="0 0 50 54" fill="none" stroke="#f07070" stroke-width="3">
      <path d="M38 18v24H10V14h22"/><path d="M16 26l8 8L44 8"/>
    </svg>
    <h3 style="margin-top:8px">IDEAS HAPPEN HERE</h3>
    <p>Clients look to us for unique, exceptional<br>solutions to their technology issues.<br>We bring creativity to the table and<br>solve your business' problems with<br>actionable solutions.</p>
  </div>
</section>

<div class="abs photo" style="left:0;top:1015px;width:600px;height:255px" role="img" aria-label="Photo of several hands stacked together in teamwork"></div>
<h2 class="abs headline" style="right:232px;top:1092px;font-size:104px;text-align:right">The<br>Cedar<br>Team</h2>
<p class="abs copy" style="right:230px;top:1380px;width:720px;text-align:right">Cedarline Studio focuses on creating extraordinary online experiences<br>for extraordinary clients. We'll work with you to create the perfect online presence for your brand.</p>
<div class="abs btn-outline" style="left:800px;top:1436px">READ MORE</div>

<h2 class="abs headline" style="left:222px;top:1508px;font-size:96px">Size<br>is everything.</h2>
<p class="abs copy" style="left:226px;top:1712px;width:740px">We don't work in a massive corporate office and we don't have a mailroom. Not that there's anything wrong with that, it's just that we like knowing each other's names, and encourage our clients to know ours. Our small staff has an advantage – our group works more efficiently, more cost-effectively and most importantly, flexible to each client's unique needs. We deliver a range of services found at any agency, with the personal service you should expect.</p>
<div class="abs btn-outline" style="left:225px;top:1830px">READ MORE</div>

<h2 class="abs headline" style="right:265px;top:1895px;font-size:100px;text-align:right">Our<br>Goal.</h2>
<div class="abs photo" style="left:40px;top:1960px;width:205px;height:415px;background:linear-gradient(180deg,#e2d3c6,#cbbfae 45%,#3d5a86 95%)" role="img" aria-label="Photo of a smiling woman standing with arms crossed"></div>
<p class="abs copy" style="right:230px;top:2052px;width:680px;text-align:right">Cedarline Studio brings your brand to life, online. We do it all when it comes to online commerce for retail stores, wholesalers and distributors. Taking your company online introduces a world of opportunity, as well as specific challenges associated with online trade. We'll assist you in establishing a successful online presence and bringing your brand to a worldwide audience.</p>
<div class="abs btn-outline" style="left:800px;top:2230px">READ MORE</div>

<section class="abs contact"></section>
<div class="abs field" style="top:2467px">your name is here</div>
<div class="abs field" style="top:2532px">Email</div>
<div class="abs field" style="top:2594px">phone</div>
<div class="abs field" style="top:2650px;height:65px">Message</div>
<div class="abs btn-login">LOGIN</div>

<div class="abs footer-dot" style="left:50px"></div>
<div class="abs footer-dot" style="left:118px"></div>
<div class="abs footer-dot" style="left:184px"></div>
<div class="abs footer-dot" style="left:252px"></div>
<p class="abs legal">© 2016 Cedarline. All rights reserved by hello@cedarline.example</p>

</body>
</html>
```